We need a corporate look website for our Company (Beit Karim for Bright Works) in Oman. We are doing Cabling Supply & Service, BMS SUpply ANd service, Fire and safety supply & Service, Video wall system supply and service, CCTV, Access control, Bio metric system, IT Software and Hardware Supply.
I will give some companies website which are doing the same business, Please refer below.
Cabling service- http://www.veltro-cablenet.com/
BMS , Video wall system, Fire and safety- http://www.qirantechgulf.com/
https://www.pqv-gl.com/
https://www.alwardasystems.com/

i have uploaded pour company letter head also. Please do the design with the same color in our logo.

```html
<!DOCTYPE html>
<html lang="en">
<head>
<meta charset="utf-8">
<title>Beit Karim – Smart Building Systems</title>
<link href="https://fonts.googleapis.com/css2?family=Montserrat:wght@500;600;700&family=Roboto:wght@400;500;700&display=swap" rel="stylesheet">
<style>
:root{
  --red:#b3151f;
  --red-dark:#8e0f17;
  --ink:#222;
  --text:#555;
  --muted:#777;
  --dark:#2b2b2b;
  --black:#151515;
  --line:#ddd;
  --white:#fff;
}
*{box-sizing:border-box;margin:0;padding:0}
html,body{width:1200px;height:3536px;overflow:hidden}
body{position:relative;background:var(--white);font-family:'Roboto',Arial,sans-serif;color:var(--text)}
.abs{position:absolute}
.heading{font-family:'Montserrat',Arial,sans-serif;font-weight:600;color:var(--ink);letter-spacing:1px;text-transform:uppercase}

/* header */
.brand{left:112px;top:24px;width:118px}
.brand-mark{width:118px;height:110px;background:var(--red)}
.brand-name{margin-top:8px;font-family:'Montserrat',sans-serif;font-weight:600;font-size:18px;color:var(--red);letter-spacing:.5px;text-align:center;text-transform:uppercase}
.topbar{right:112px;top:54px;font-size:15px;color:#444;display:flex;align-items:center;gap:12px}
.topbar svg{width:15px;height:15px;fill:var(--red)}
.topbar .sep{color:#aaa;margin:0 14px}
.nav{right:112px;top:110px;display:flex;gap:25px;align-items:center;font-family:'Montserrat',sans-serif;font-weight:600;font-size:16px;color:#222}
.nav svg{width:17px;height:17px}

/* hero */
.hero{left:0;top:185px;width:1200px;height:560px;background:radial-gradient(circle at 50% 45%,#e9a25a 0%,#8a4a22 22%,#2e2a2c 55%,#151a22 100%)}
.hero-title{left:0;top:380px;width:1200px;text-align:center;font-family:'Montserrat',sans-serif;font-weight:500;font-size:62px;color:var(--white);letter-spacing:2px}

/* services */
.section-title{left:0;width:1200px;text-align:center;font-size:42px}
.card{top:955px;width:226px;height:360px;background:var(--white);box-shadow:0 2px 8px rgba(0,0,0,.15);text-align:center}
.card-img{height:165px;margin:2px}
.card h3{font-family:'Roboto',sans-serif;font-weight:700;font-size:18px;color:#333;text-transform:uppercase;line-height:25px;margin:32px 14px 12px}
.card p{font-size:14px;line-height:22px;color:var(--muted);margin:0 22px}
.btn{display:inline-flex;align-items:center;justify-content:center;gap:6px;font-family:'Roboto',sans-serif;font-weight:700;font-size:15px;text-transform:uppercase;background:var(--red);color:var(--white)}
.slide-arrow{width:30px;height:48px;background:var(--white);border:1px solid #ccc;display:flex;align-items:center;justify-content:center}
.slide-arrow.red{background:var(--red);border-color:var(--red)}

/* quote */
.quote-title{left:0;top:1605px;width:1200px;text-align:center;font-family:'Montserrat',sans-serif;font-weight:600;font-size:40px;color:var(--white);letter-spacing:1px}
.quote-text{left:0;top:1678px;width:1200px;text-align:center;font-weight:700;font-size:16px;color:var(--white)}
.quote-btn{left:505px;top:1733px;width:190px;height:42px;background:var(--white);color:var(--red)}

/* about */
.ghost{font-family:'Montserrat',sans-serif;font-weight:700;color:rgba(0,0,0,.06);text-transform:uppercase;white-space:nowrap}
.about-title{left:112px;top:2035px;font-size:44px}
.about-copy{left:112px;top:2118px;width:456px;font-size:15px;line-height:25px;color:var(--muted);text-align:justify}
.about-copy p+p{margin-top:22px}
.about-btn{left:112px;top:2338px;width:168px;height:48px;border-radius:24px}
.video{left:628px;top:2066px;width:470px;height:300px;background:linear-gradient(135deg,#c9d3dc 0%,#e7e2dc 45%,#b08e74 75%,#6c7a88 100%)}
.corner{width:34px;height:34px;border:5px solid var(--red)}
.divider{left:112px;top:2513px;width:976px;height:1px;background:var(--line)}

/* clients */
.clients-text{left:240px;top:2685px;width:720px;text-align:center;font-size:15px;line-height:25px;color:var(--muted)}
.client{top:2770px;width:176px;height:86px;border:1px solid #ccc;background:var(--white);display:flex;align-items:center;justify-content:center;gap:8px;font-family:'Roboto',sans-serif;font-weight:500;font-size:16px;color:#444}
.client i{width:16px;height:16px;background:#666;border-radius:50%;display:block}

/* footer */
.foot-col{top:3185px;color:#ddd;font-size:14px}
.foot-col h4{font-family:'Roboto',sans-serif;font-weight:700;font-size:16px;color:var(--white);text-decoration:underline;text-transform:uppercase;margin-bottom:22px}
.foot-col li{list-style:none;margin-bottom:18px;display:flex;gap:10px;align-items:center}
.foot-col li:before{content:"»";color:#ddd}
.news-input{width:268px;height:38px;border:1px solid #bbb;color:#ccc;font-size:12px;padding:11px 10px;margin-top:12px}
.news-btn{width:100px;height:36px;border-radius:18px;margin-top:12px;font-size:14px}
.contact li:before{content:none}
.contact li{align-items:flex-start;line-height:21px;margin-bottom:20px}
.contact svg{width:18px;height:18px;fill:#aaa;flex:none;margin:2px 14px 0 0}
.social{left:0;top:3412px;width:1200px;display:flex;justify-content:center;align-items:center;gap:10px}
.social .rule{width:310px;height:1px;background:#666}
.social span{width:40px;height:40px;border:2px solid #ddd;border-radius:50%;display:block}
.copy{left:0;top:3480px;width:1200px;text-align:center;font-size:14px;color:#ddd}
</style>
</head>
<body>

<!-- header -->
<div class="abs brand">
  <div class="brand-mark"></div>
  <div class="brand-name">Beit Karim</div>
</div>
<div class="abs topbar">
  <svg viewBox="0 0 24 24"><path d="M6.6 10.8a15.1 15.1 0 0 0 6.6 6.6l2.2-2.2a1 1 0 0 1 1-.25 11.4 11.4 0 0 0 3.6.57 1 1 0 0 1 1 1V20a1 1 0 0 1-1 1A17 17 0 0 1 3 4a1 1 0 0 1 1-1h3.5a1 1 0 0 1 1 1c0 1.25.2 2.45.57 3.57a1 1 0 0 1-.25 1z"/></svg>
  <span>968 555 01942</span>
  <span class="sep">|</span>
  <svg viewBox="0 0 24 24"><path d="M2 5h20v14H2z M2 5l10 8 10-8" fill="none" stroke="#b3151f" stroke-width="2"/></svg>
  <span>info@beitkarim.com</span>
</div>
<nav class="abs nav">
  <span>HOME</span><span>ABOUT US</span><span>SOLUTIONS</span><span>SERVICES</span><span>NEWS</span><span>CONTACT</span>
  <svg viewBox="0 0 24 24" fill="none" stroke="#222" stroke-width="3"><circle cx="10" cy="10" r="7"/><path d="M15 15l7 7"/></svg>
</nav>

<!-- hero -->
<div class="abs hero" role="img" aria-label="Finger touching a glowing fingerprint scanner interface"></div>
<div class="abs hero-title">BIO METRIC SYSTEM</div>
<svg class="abs" style="left:0;top:620px" width="1200" height="140" viewBox="0 0 1200 140">
  <polygon points="0,125 1200,40 1200,140 0,140" fill="#fff"/>
  <polygon points="520,105 1200,40 1200,75 700,120" fill="#b3151f"/>
</svg>

<!-- services -->
<div class="abs" style="left:380px;top:780px;width:560px;height:420px;background:radial-gradient(ellipse,rgba(0,0,0,.05),rgba(0,0,0,0) 70%)" role="img" aria-label="Faint security camera in the background"></div>
<h2 class="abs heading section-title" style="top:838px">Our Services</h2>

<div class="abs slide-arrow red" style="left:0;top:1110px"><svg width="12" height="18" viewBox="0 0 12 18"><path d="M10 2L3 9l7 7" fill="none" stroke="#fff" stroke-width="2.5"/></svg></div>
<div class="abs slide-arrow" style="right:0;top:1110px"><svg width="12" height="18" viewBox="0 0 12 18"><path d="M2 2l7 7-7 7" fill="none" stroke="#b3151f" stroke-width="2.5"/></svg></div>

<div class="abs card" style="left:112px">
  <div class="card-img" role="img" aria-label="Technician connecting network cables" style="background:linear-gradient(135deg,#c0611f,#3a5c8a 60%,#1e2a3a)"></div>
  <h3>Cabling Supply<br>&amp; Service</h3>
  <p>Lorem ipsum dolor sit amet consectetur adipiscing elited do eiusmod tempor.</p>
</div>
<div class="abs card" style="left:363px">
  <div class="card-img" role="img" aria-label="Electrical substation equipment" style="background:linear-gradient(180deg,#bcc6b4,#6d5448 60%,#4a4a3c)"></div>
  <h3>BMS Supply and<br>Service</h3>
  <p>Lorem ipsum dolor sit amet consectetur adipiscing elited do eiusmod tempor.</p>
</div>
<div class="abs card" style="left:612px">
  <div class="card-img" role="img" aria-label="Smoke detector on a ceiling with smoke" style="background:linear-gradient(180deg,#d6d6d6,#8d8d8d 70%,#5e5e5e)"></div>
  <h3>Fire and Safety<br>Supply</h3>
  <p>Lorem ipsum dolor sit amet consectetur adipiscing elited do eiusmod tempor.</p>
</div>
<div class="abs card" style="left:862px">
  <div class="card-img" role="img" aria-label="Hand holding an access card to a reader" style="background:linear-gradient(135deg,#3c3f48,#8b8f98 55%,#c8a690)"></div>
  <h3>Bio Metric System<br>Services</h3>
  <p>Lorem ipsum dolor sit amet consectetur adipiscing elited do eiusmod tempor.</p>
</div>
<div class="abs btn" style="left:393px;top:1310px;width:162px;height:40px">Read More
  <svg width="14" height="14" viewBox="0 0 14 14"><circle cx="7" cy="7" r="7" fill="#fff"/><path d="M5.5 4l3 3-3 3" fill="none" stroke="#b3151f" stroke-width="2"/></svg></div>

<!-- quote band -->
<svg class="abs" style="left:0;top:1470px" width="1200" height="460" viewBox="0 0 1200 460">
  <polygon points="0,5 560,40 0,85" fill="#2b2b2b"/>
  <polygon points="0,85 560,40 1200,0 1200,355 760,395 0,450" fill="#b3151f"/>
  <polygon points="660,400 1200,355 1200,440" fill="#2b2b2b"/>
</svg>
<div class="abs quote-title">GET A FREE QUOTE</div>
<div class="abs quote-text">Lorem ipsum dolor sit amet consectetur adipiscing elit sed do eiusmod tempor incididunt.</div>
<div class="abs btn quote-btn">Get a Quote
  <svg width="14" height="14" viewBox="0 0 14 14"><circle cx="7" cy="7" r="7" fill="#b3151f"/><path d="M5.5 4l3 3-3 3" fill="none" stroke="#fff" stroke-width="2"/></svg></div>

<!-- about -->
<div class="abs ghost" style="left:6px;top:2015px;font-size:88px">Who We Are</div>
<h2 class="abs heading about-title">About Us</h2>
<div class="abs about-copy">
  <p>Lorem ipsum dolor sit amet, consectetur adipiscing elit, sed do eiusmod tempor incididunt ut labore et dolore magna aliqua.</p>
  <p>Ut enim ad minim veniam, quis nostrud exercitation ullamco laboris nisi ut aliquip ex ea commodo consequat. Duis aute irure dolor in reprehenderit in voluptate velit esse cillum dolore eu fugiat nulla pariatur. Excepteur sint occaecat cupidatat.</p>
</div>
<div class="abs btn about-btn">Read More
  <svg width="14" height="14" viewBox="0 0 14 14"><circle cx="7" cy="7" r="7" fill="#fff"/><path d="M5.5 4l3 3-3 3" fill="none" stroke="#b3151f" stroke-width="2"/></svg></div>

<div class="abs corner" style="left:618px;top:2056px;border-right:none;border-bottom:none"></div>
<div class="abs corner" style="left:1074px;top:2056px;border-left:none;border-bottom:none"></div>
<div class="abs corner" style="left:618px;top:2342px;border-right:none;border-top:none"></div>
<div class="abs corner" style="left:1074px;top:2342px;border-left:none;border-top:none"></div>
<div class="abs video" role="img" aria-label="Video still of a technician installing a wall-mounted security sensor"></div>
<svg class="abs" style="left:831px;top:2190px" width="64" height="50" viewBox="0 0 64 50">
  <circle cx="32" cy="25" r="24" fill="rgba(0,0,0,.55)"/>
  <path d="M26 15l16 10-16 10z" fill="#fff"/>
</svg>

<div class="abs divider"></div>

<!-- clients -->
<div class="abs ghost" style="left:0;top:2598px;width:1200px;text-align:center;font-size:86px">Our Clients</div>
<h2 class="abs heading section-title" style="top:2612px">Our Clients</h2>
<p class="abs clients-text">Lorem ipsum dolor sit amet, consectetur adipiscing elit, sed do eiusmod tempor incididunt ut labore et dolore magna aliqua. Ut enim ad minim veniam nostrud exercitation ullamco laboris nisi.</p>
<svg class="abs" style="left:58px;top:2802px" width="14" height="22" viewBox="0 0 14 22"><path d="M11 2L3 11l8 9" fill="none" stroke="#888" stroke-width="2"/></svg>
<svg class="abs" style="left:1128px;top:2802px" width="14" height="22" viewBox="0 0 14 22"><path d="M3 2l8 9-8 9" fill="none" stroke="#888" stroke-width="2"/></svg>
<div class="abs client" style="left:112px"><i></i>Harbor City Hospital</div>
<div class="abs client" style="left:312px"><i></i>Kindred Relief</div>
<div class="abs client" style="left:512px"><i></i>Slatebrook</div>
<div class="abs client" style="left:712px"><i></i>Meridian Staffing</div>
<div class="abs client" style="left:912px"><i></i>Skill Guild</div>

<!-- footer -->
<svg class="abs" style="left:0;top:2970px" width="1200" height="566" viewBox="0 0 1200 566">
  <polygon points="0,5 1200,80 1200,120 0,90" fill="#b3151f"/>
  <polygon points="0,75 1200,120 1200,566 0,566" fill="#151515"/>
</svg>

<div class="abs foot-col" style="left:112px">
  <h4>Company</h4>
  <ul><li>Home</li><li>About Us</li><li>Our Services</li><li>Solutions</li></ul>
</div>
<div class="abs foot-col" style="left:290px">
  <h4>Resources</h4>
  <ul><li>Contact Us</li><li>Book A Callback</li><li>FAQs</li><li>Terms &amp; Conditions</li></ul>
</div>
<div class="abs foot-col" style="left:507px;width:290px">
  <h4>Join Our Newsletter</h4>
  <p style="line-height:20px">Sign up for our newsletter to stay up-to-date with our Company Informations</p>
  <div class="news-input">Email Address</div>
  <div class="btn news-btn">Submit</div>
</div>
<div class="abs foot-col contact" style="left:858px;width:240px">
  <h4>Contact Details</h4>
  <ul>
    <li><svg viewBox="0 0 24 24"><path d="M12 2a7 7 0 0 0-7 7c0 5 7 13 7 13s7-8 7-13a7 7 0 0 0-7-7zm0 9.5A2.5 2.5 0 1 1 12 6.5a2.5 2.5 0 0 1 0 5z"/></svg>48 Harbour Road, Suite 210<br>Ruwi, Muscat 112.</li>
    <li><svg viewBox="0 0 24 24"><path d="M6.6 10.8a15.1 15.1 0 0 0 6.6 6.6l2.2-2.2a1 1 0 0 1 1-.25 11.4 11.4 0 0 0 3.6.57 1 1 0 0 1 1 1V20a1 1 0 0 1-1 1A17 17 0 0 1 3 4a1 1 0 0 1 1-1h3.5a1 1 0 0 1 1 1c0 1.25.2 2.45.57 3.57a1 1 0 0 1-.25 1z"/></svg>(+968) 2455 0194</li>
    <li><svg viewBox="0 0 24 24"><path d="M2 5h20v14H2z M2 5l10 8 10-8" fill="none" stroke="#aaa" stroke-width="2"/></svg>support@beitkarim.com</li>
  </ul>
</div>

<div class="abs social">
  <div class="rule"></div>
  <span></span><span></span><span></span><span></span>
  <div class="rule"></div>
</div>
<div class="abs copy">Copyrights © 2019 Beit Karim. All Rights Reserved &nbsp; | &nbsp; Privacy Policy</div>

</body>
</html>
```